New Stationery Design Project

We got a project done from you for Pravonix stationary design. We have changed the name of the company from Pravonix to Kelmra.
So we want to redesign our stationay.
We are a VOIP, hosted pbx, and cloud services provider. Clients are mostly hotels, offices, business etc. needing phone services.
Our Slogan is : "Low cost, high quality service"
the logo has to be changed from Pravonix to Kelmra
Business address is
4172 Marrow Pkwy, suite 210
Dallas TX 75399
Phone: 555-013-4872
Fax: 555-013-4872
Website: Kelmra.example
Industry/Entity Type
Business
Look and feel
Each slider illustrates characteristics of the customer's brand and the style your logo design should communicate.

```html
<!DOCTYPE html>
<html lang="en">
<head>
<meta charset="utf-8">
<title>Kelmra Business Card</title>
<link rel="stylesheet" href="https://fonts.googleapis.com/css2?family=Quicksand:wght@500;600;700&display=swap">
<style>
  :root {
    --bg: #e9eaee;
    --card-white: #f6f7f9;
    --ink: #222222;
    --band: #2a2a2a;
    --band-text: #e8e8e8;
    --accent-green: #9acd1e;
    --accent-blue: #1ba3e0;
    --accent-pink: #e6177f;
    --accent-orange: #f0851d;
    --shadow: 0 6px 18px rgba(0, 0, 0, 0.14);
  }
  * { box-sizing: border-box; margin: 0; padding: 0; }
  html, body {
    width: 1200px;
    height: 934px;
    overflow: hidden;
    background: var(--bg);
    font-family: "Quicksand", sans-serif;
    color: var(--ink);
  }
  .canvas {
    position: relative;
    width: 1200px;
    height: 934px;
  }
  .card {
    position: absolute;
    width: 560px;
    height: 320px;
    box-shadow: var(--shadow);
    overflow: hidden;
  }
  /* Back of card */
  .card-back {
    left: 70px;
    top: 110px;
    background: var(--band);
    display: flex;
    align-items: center;
    justify-content: center;
  }
  .card-back .wordmark {
    color: var(--card-white);
    font-size: 40px;
    font-weight: 600;
    letter-spacing: 4px;
  }
  /* Front of card */
  .card-front {
    left: 570px;
    top: 500px;
    background: var(--card-white);
  }
  .holder {
    position: absolute;
    top: 46px;
    right: 40px;
    text-align: right;
  }
  .holder-name {
    font-size: 19px;
    font-weight: 700;
    letter-spacing: 0.3px;
  }
  .holder-role {
    font-size: 13px;
    font-weight: 500;
  }
  .brand {
    position: absolute;
    left: 38px;
    top: 112px;
    display: flex;
    align-items: center;
    gap: 14px;
  }
  .brand-dot {
    width: 44px;
    height: 44px;
    border-radius: 50%;
    background: var(--accent-pink);
    flex: none;
  }
  .brand-text .wordmark {
    font-size: 40px;
    font-weight: 600;
    letter-spacing: 4px;
    line-height: 1;
    color: var(--ink);
  }
  .tagline {
    font-size: 16px;
    font-weight: 500;
    margin-top: 6px;
  }
  .contact-band {
    position: absolute;
    left: 0;
    bottom: 0;
    width: 100%;
    height: 92px;
    background: var(--band);
  }
  .contact {
    position: absolute;
    left: 30px;
    bottom: 18px;
    color: var(--band-text);
    font-size: 13.5px;
    font-weight: 500;
    line-height: 1.6;
  }
  .contact .label-phone { color: var(--accent-green); font-weight: 700; }
  .contact .label-fax { color: var(--accent-blue); font-weight: 700; }
  .bubble-art {
    position: absolute;
    right: 0;
    bottom: 0;
    width: 160px;
    height: 118px;
    background: linear-gradient(135deg, var(--accent-blue) 0%, var(--accent-orange) 35%, var(--accent-pink) 65%, var(--accent-green) 100%);
    opacity: 0.9;
  }
</style>
</head>
<body>
  <main class="canvas">
    <section class="card card-back" aria-label="Business card back">
      <span class="wordmark">KELMRA</span>
    </section>

    <section class="card card-front" aria-label="Business card front">
      <div class="holder">
        <p class="holder-name">DANA WHITFIELD</p>
        <p class="holder-role">Manager</p>
      </div>

      <div class="brand">
        <span class="brand-dot"></span>
        <div class="brand-text">
          <p class="wordmark">KELMRA</p>
          <p class="tagline">Low cost, high quality service</p>
        </div>
      </div>

      <div class="contact-band"></div>
      <div class="bubble-art" role="img" aria-label="Cluster of colourful speech bubbles with greetings"></div>
      <address class="contact">
        4172 Marrow Pkwy, Suite 210, Dallas TX 75399<br>
        <span class="label-phone">T:</span> 555-013-4872 · <span class="label-fax">F:</span> 555-013-4873 · www.kelmra.example
      </address>
    </section>
  </main>
</body>
</html>
```